Product labels for new supplements business targeting high performing creative people

I need a label design for different supplements like Whey, BCAA, Melatonin etc. that I could customize for each use case separately.

The brand is called lanternfolk.life, and it would be the first design of the labels. We haven't sold any products yet, but the target audience is people with growth mindset, people who want to be as efficient as possible and are constantly looking to improve their lifestyle. As part of that, they are also working out, but don't know much about supplements yet. Mostly people between 20-34.

I don't have a too specific idea of the expected design, though it should be light, warm, smart and minimalist, maybe have some patterns. It should looks smart and clean (and expensive). Orange and golden might be the additional colors for white. I have attached the templates of some products that I plan to sell and also the logo of the brand.

Here's what I have used for inspiration:
Brands that I like and are somewhat similar in concept: https://www.vimqera.com/ (!!specially the way they
bring "how the product helps them" in focus, not "what the product is" & https://www.pobri.care/ &
https://www.selvoda.com/sport/ & https://en.kambelo.fr/ &
https://gridmarket.com/profiles/corawellhaldesign/designs/417586

Here's how different products look like: https://prodaxel.com/catalog

Target Market(s)

target audience is people with growth mindset, people who want to be as efficient as possible and are constantly looking to improve their lifestyle. As part of that, they are also working out, but don't know much about supplements yet. Mostly people between 20-34.

Industry/Entity Type

Supplements

Font styles to use
Sans Serif

Colors
FFC000
F8CF3A
FAE287
FDF2CF
FEFAEE
F0912C
F2A743
F7CA91
FBE8D2
FDF5EE
EE7325
F08F49
F5BC92
FAE3D3
FDF4ED

Requirements
Must have
• Clean, smart and minimalist design that can be applied for different products in different sizes, like Whey protein, BCAA, vitamins etc. available here: https://prodaxel.com/catalog
Nice to have
• Patterns, expensive look
Should not have
• Doodles, too many colors

```html
<!DOCTYPE html>
<html lang="en">
<head>
<meta charset="utf-8">
<title>lanternfolk.life — Melatonin label</title>
<link rel="stylesheet" href="https://fonts.googleapis.com/css2?family=Catamaran:wght@500;600&family=Montserrat:wght@800&family=Hind:wght@400&display=swap">
<style>
  :root {
    --page: #fbfcfe;
    --label-dark: #1a1110;
    --label-mid: #2a1f1d;
    --ink-light: #ffffff;
    --ink-soft: #e9e3e1;
    --orange: #f0912c;
    --orange-deep: #ee7325;
    --orange-red: #e2532a;
  }
  * { margin: 0; padding: 0; box-sizing: border-box; }
  html, body {
    width: 1200px;
    height: 1000px;
    overflow: hidden;
    background: var(--page);
  }
  .canvas {
    position: relative;
    width: 1200px;
    height: 1000px;
    background: var(--page);
  }
  .label {
    position: absolute;
    left: 300px;
    top: 66px;
    width: 600px;
    height: 867px;
    background: linear-gradient(135deg, var(--label-mid) 0%, var(--label-dark) 45%, var(--label-mid) 100%);
    color: var(--ink-light);
    overflow: hidden;
  }
  .brand {
    position: absolute;
    top: 200px;
    left: 0;
    width: 100%;
    display: flex;
    justify-content: center;
    align-items: center;
    gap: 12px;
  }
  .brand-dot {
    width: 14px;
    height: 14px;
    border-radius: 50%;
    background: var(--orange-deep);
  }
  .brand-name {
    font-family: "Catamaran", sans-serif;
    font-weight: 600;
    font-size: 42px;
    line-height: 1;
    color: var(--ink-light);
    letter-spacing: 0.5px;
  }
  .product-name {
    position: absolute;
    top: 352px;
    left: 56px;
    width: 488px;
    text-align: center;
    font-family: "Montserrat", sans-serif;
    font-weight: 800;
    font-size: 70px;
    line-height: 1;
    letter-spacing: 1px;
    color: var(--ink-light);
  }
  .product-dose {
    position: absolute;
    top: 432px;
    right: 56px;
    font-family: "Catamaran", sans-serif;
    font-weight: 600;
    font-size: 36px;
    line-height: 1;
    color: var(--ink-light);
  }
  .chevron {
    position: absolute;
    left: 0;
    top: 0;
    width: 600px;
    height: 867px;
  }
  .benefits {
    position: absolute;
    top: 614px;
    left: 334px;
    list-style: none;
    font-family: "Hind", sans-serif;
    font-weight: 400;
    font-size: 25px;
    line-height: 31px;
    letter-spacing: 0.6px;
    color: var(--ink-soft);
  }
  .benefits sup {
    font-size: 14px;
    vertical-align: top;
    line-height: 1;
  }
  .footer {
    position: absolute;
    top: 806px;
    left: 54px;
    right: 52px;
    display: flex;
    justify-content: space-between;
    font-family: "Catamaran", sans-serif;
    font-weight: 500;
    font-size: 24px;
    line-height: 1;
    letter-spacing: 0.8px;
    color: var(--ink-soft);
  }
</style>
</head>
<body>
  <main class="canvas">
    <section class="label">
      <div class="brand">
        <span class="brand-dot"></span>
        <span class="brand-name">lanternfolk.life</span>
      </div>

      <h1 class="product-name">MELATONIN</h1>
      <p class="product-dose">1 mg</p>

      <svg class="chevron" viewBox="0 0 600 867" aria-hidden="true">
        <defs>
          <linearGradient id="chevron-fill" x1="0" y1="0" x2="1" y2="0">
            <stop offset="0" stop-color="var(--orange)"/>
            <stop offset="0.6" stop-color="var(--orange-deep)"/>
            <stop offset="1" stop-color="var(--orange-red)"/>
          </linearGradient>
        </defs>
        <polygon points="226,542 542,527 302,600 289,762" fill="url(#chevron-fill)"/>
      </svg>

      <ul class="benefits">
        <li>Fall asleep faster<sup>*</sup></li>
        <li>Stay asleep longer<sup>*</sup></li>
      </ul>

      <div class="footer">
        <span class="footer-type">DIETARY SUPPLEMENT</span>
        <span class="footer-count">60 TABLETS</span>
      </div>
    </section>
  </main>
</body>
</html>
```